New DL Brochures for Kites Gymnastics Centres

Kites Gymnastics is about to launch its new website and to coincide with this we would like to produce a complete new set of brochures for all of our programs (10 programs)
Kites Gymnastics provides sports coaching for young children in gymnastics lessons as well as conducting holiday programs and birthday parties.
Our company colours are red, gold and black but we are trying to maintain a clean, sharp image so lots of white should be used to highlight our colours.
The brochures should all follow the same template and be clean, fresh, simple and exciting making you want to use our services.
Each brochure should contain 1 or 2 pictures (you decide !) as well as our logo (ideally at the top) with our contact details at the bottom (contact details will be required to be changed for each of our 4 locations)
We have a supply of images which will replace the stock photo supplied for the winning bid.
UPDATE - I will consider postcard type designs which may allow a more diverse range of ideas - this could be very effective way to display the information
Updates
Project Deadline Extended
Reason: I have increased the budget and would like to encourage more designs :)
I am now considering postcard type designs for this project as well as DL sized designs. After looking over a couple of designs it may be possible to do a great "postcard" style design with a great picture and basic info on the front and program info on the back of the postcard
Hi All,
Target Market(s)
Parents of young children
Industry/Entity Type
It Company
Look and feel
Each slider illustrates characteristics of the customer's brand and the style your logo design should communicate.

```html
<!DOCTYPE html>
<html lang="en">
<head>
<meta charset="utf-8">
<title>Mini Kites – Kites Gymnastics</title>
<link rel="stylesheet" href="https://fonts.googleapis.com/css2?family=Arimo:wght@400;700&family=Open+Sans:wght@300;400;600;700&display=swap">
<style>
  :root {
    --red: #e31b23;
    --red-deep: #b5121b;
    --red-soft: #ee4a4f;
    --gold: #f5b335;
    --ink: #1d1d1b;
    --text: #4a4a4a;
    --white: #ffffff;
  }
  * { box-sizing: border-box; margin: 0; padding: 0; }
  html, body { width: 826px; height: 1200px; overflow: hidden; background: var(--white); }
  .brochure {
    position: relative;
    width: 826px;
    height: 1200px;
    overflow: hidden;
    background: var(--white);
    font-family: "Open Sans", Arial, sans-serif;
    color: var(--text);
  }
  .award-tag {
    position: absolute; left: 55px; top: 36px; width: 258px; height: 31px;
    background: var(--red);
    color: var(--gold);
    font-family: "Arimo", Arial, sans-serif;
    font-size: 18px; line-height: 31px; text-align: center;
  }
  .brand {
    position: absolute; left: 55px; top: 92px;
    display: flex; align-items: center; gap: 16px;
  }
  .brand-name {
    font-family: "Open Sans", Arial, sans-serif;
    font-weight: 700; font-size: 42px; line-height: 1;
    color: var(--ink); letter-spacing: -0.5px;
  }
  .brand-dot { width: 52px; height: 52px; border-radius: 50%; background: var(--red); }
  .promise {
    position: absolute; left: 557px; top: 42px; width: 230px; height: 135px;
    background: var(--red);
    color: var(--white);
    font-family: "Arimo", Arial, sans-serif;
    font-weight: 700; font-size: 19px; line-height: 27.7px;
    text-align: center; padding-top: 13px;
    box-shadow: 2px 3px 4px rgba(0,0,0,0.25);
  }
  .offer {
    position: absolute; left: 0; top: 206px; width: 826px;
    text-align: center;
    font-family: "Arimo", Arial, sans-serif;
    font-size: 19px; line-height: 24px; color: var(--red);
  }
  .program-title {
    position: absolute; left: 62px; top: 242px;
    font-family: "Arimo", Arial, sans-serif;
    font-size: 80px; line-height: 1; font-weight: 400;
    color: var(--red); letter-spacing: 0.5px; white-space: nowrap;
    text-shadow: 2px 3px 3px rgba(0,0,0,0.28);
  }
  .title-rule {
    position: absolute; left: 62px; top: 322px; width: 400px; height: 2px;
    background: var(--red);
  }
  .age-range {
    position: absolute; left: 184px; top: 328px;
    font-family: "Arimo", Arial, sans-serif;
    font-size: 21px; line-height: 26px; color: var(--red);
  }
  .hero-photo { position: absolute; left: 522px; top: 232px; }
  .intro {
    position: absolute; left: 55px; top: 366px; width: 600px;
    font-size: 15px; line-height: 21.6px; color: var(--text);
  }
  .intro p:first-child { width: 455px; }
  .intro p:last-child { text-align: justify; }
  .quote-band {
    position: absolute; left: 0; top: 652px; width: 826px; height: 118px;
    background: linear-gradient(to bottom, var(--red-soft) 0%, var(--red) 35%, var(--red-deep) 100%);
    display: flex; align-items: center; justify-content: center;
  }
  .quote {
    font-family: "Arimo", Arial, sans-serif;
    font-weight: 700; font-size: 24px; line-height: 32px;
    color: var(--gold); text-align: center;
  }
  .benefits { position: absolute; left: 222px; top: 780px; list-style: none; }
  .benefits li {
    font-size: 16.4px; line-height: 23.5px; color: var(--text);
    position: relative; padding-left: 18px;
  }
  .benefits li::before {
    content: ""; position: absolute; left: 2px; top: 10px;
    width: 5px; height: 5px; border-radius: 50%; background: var(--text);
  }
  .benefits li:nth-child(2) { margin-left: 14px; }
  .benefits li:nth-child(3) { margin-left: 28px; }
  .benefits li:nth-child(4) { margin-left: 42px; }
  .benefits li:nth-child(5) { margin-left: 56px; width: 470px; }
  .footer-swoosh { position: absolute; left: 0; top: 900px; }
  .coach-photo { position: absolute; left: 39px; top: 808px; }
  .contact {
    position: absolute; left: 579px; top: 1024px;
    color: var(--white); font-style: normal;
  }
  .contact-heading {
    font-family: "Open Sans", Arial, sans-serif;
    font-weight: 300; font-size: 30px; line-height: 40px;
  }
  .contact-line {
    font-family: "Open Sans", Arial, sans-serif;
    font-weight: 300; font-size: 17px; line-height: 22px; letter-spacing: 0.5px;
    margin-top: 22px;
  }
</style>
</head>
<body>
<main class="brochure">
  <div class="award-tag">2012 WAG Club of the Year</div>

  <div class="brand">
    <span class="brand-name">KITES GYMNASTICS</span>
    <span class="brand-dot" aria-hidden="true"></span>
  </div>

  <div class="promise">Qualified Instructors<br>Great Facilities<br>Safe<br>Fun</div>

  <p class="offer">Give your child the best start in life - Book NOW for a Free Mini Kites Try Out Class</p>

  <h1 class="program-title">MINI KITES</h1>
  <div class="title-rule"></div>
  <p class="age-range">(2-6 years)</p>

  <svg class="hero-photo" width="268" height="200" viewBox="0 0 268 200" role="img" aria-label="Photo of three young girls in leotards sitting with arms raised">
    <defs>
      <linearGradient id="heroFill" x1="0" y1="0" x2="1" y2="1">
        <stop offset="0" stop-color="#d8d8da"/>
        <stop offset="1" stop-color="#a9aaae"/>
      </linearGradient>
    </defs>
    <polygon points="6,4 266,4 266,96 38,196 6,150" fill="#6f7074"/>
    <polygon points="2,10 260,10 260,96 36,196 2,150" fill="url(#heroFill)"/>
  </svg>

  <div class="intro">
    <p>The Mini Kites Program is designed to give children 2-6 years of age the best start in life. At Kites we use gymnastics to teach children how to move their bodies in a huge variety of ways including running, jumping, rolling, swinging, balancing, landing, hopping, cartwheeling, spinning, and so much more.</p>
    <p>Mini Kites incorporates all of our wonderful gymnastics apparatus such as ropes, rings, trampolines, balance beam, bars and also uses our huge sprung floor area with loads of soft shapes which encourage learning. Each Mini Kites class combines themes with gymnastics skills and concepts such as colours, numbers, shapes etc, which helps students maximise their learning opportunities.</p>
  </div>

  <div class="quote-band">
    <p class="quote">“Gymnastics&nbsp; teaches&nbsp; everything - life lessons,<br>responsibility and discipline and respect”</p>
  </div>

  <ul class="benefits">
    <li>Develops amazing self confidence</li>
    <li>Builds spatial awareness</li>
    <li>Builds strength, coordination and flexibility</li>
    <li>Improves the vestibular system – important for brain learning</li>
    <li>Loads of Fun for kids to explore their bodies amazing capabilities</li>
  </ul>

  <svg class="footer-swoosh" width="826" height="300" viewBox="0 0 826 300" aria-hidden="true">
    <defs>
      <linearGradient id="swooshFill" x1="0" y1="0" x2="0.4" y2="1">
        <stop offset="0" stop-color="#ee3b40"/>
        <stop offset="1" stop-color="#b5121b"/>
      </linearGradient>
    </defs>
    <path d="M826,0 C700,40 450,70 330,110 C250,140 230,190 230,300 L826,300 Z" fill="url(#swooshFill)"/>
    <path d="M826,60 C690,95 470,110 360,150 C300,175 285,215 300,260" fill="none" stroke="#ffffff" stroke-width="9" opacity="0.9"/>
    <path d="M826,90 C700,120 500,140 400,170" fill="none" stroke="#ffffff" stroke-width="2" opacity="0.5"/>
  </svg>

  <svg class="coach-photo" width="270" height="392" viewBox="0 0 270 392" role="img" aria-label="Photo of a coach helping a young child climb a wooden ladder frame">
    <defs>
      <linearGradient id="coachFill" x1="0" y1="0" x2="0" y2="1">
        <stop offset="0" stop-color="#cfcfd1"/>
        <stop offset="1" stop-color="#a7a8ac"/>
      </linearGradient>
    </defs>
    <polygon points="135,3 268,110 268,392 2,392 2,110" fill="url(#coachFill)"/>
  </svg>

  <address class="contact">
    <p class="contact-heading">Address</p>
    <p class="contact-line">LOREMIPSUM</p>
    <p class="contact-line">LOREMIPSUM</p>
    <p class="contact-line">LOREMIPSUM</p>
  </address>
</main>
</body>
</html>
```